Counselling practice needs a Business Card Design

I need a business card design for a new counselling practice in Canberra, Australia. The name of the practice is Dr Henry Walsh, Counselling Services and the practice focuses on philosophical, narrative and existential counselling for individuals, couples and families. The final design should communicate professionalism, sophistication of analysis and psychological wholeness. The reverse side of the card should have an appointment reminder
Updates

Could the following qualifications also be included on card. BSc (Psychology), BA hons (Philosophy), PhD (Philosophy), Diploma of Community Counselling And the following affiliation Guild of Talk Therapists of Tasvale and District Inc. (GOTTTD) And my contact phone mobile phone number is 0455837190, and email is Henry.Walsh937@mailbrook.example for inclusion as well.

Thank you all who have put in a design so far. I just wanted to clarify some design points based on what you have submitted. 1. The Guild of Talk Therapists. Tasvale and District Inc. (GOTTTD) is an affiliation only. 'Member of the Guild of Talk Therapists. Tasvale and District Inc (GOTTTD)' should appear with the same prominence of a qualification. 2. The Post Graduate Diploma in Community Counselling is a quaification and should appear as 'PG Dip (Community Counselling)' after the other qualifications. 3. I am advertising myself as a counsellor so 'Dr Henry Walsh, Counselling Services' or 'Dr Henry Walsh, Counsellor' is the equivalent of the business name. After looking at some of the designs I prefer Dr Henry Walsh in sentence case rather than all capitals (DR HENRY WALSH). 4. 'Philosophical, narrative and existential counselling for individuals, couples and families' is the description of the type of counselling services and should appear on the card.

One further point. I have updated my email address for the card. It is now drhenrywalsh@tasvaletherapy.example

```html
<!DOCTYPE html>
<html lang="en">
<head>
<meta charset="utf-8">
<title>Dr Henry Walsh – Business Cards</title>
<link href="https://fonts.googleapis.com/css2?family=Arimo:wght@400;700&display=swap" rel="stylesheet">
<style>
  :root {
    --navy: #0c2249;
    --white: #ffffff;
    --ink: #1b1b1b;
    --muted: #c9d1df;
    --stage: #e6e4e0;
  }
  html, body {
    margin: 0;
    padding: 0;
    width: 1200px;
    height: 784px;
    overflow: hidden;
    background: var(--stage);
    font-family: "Arimo", Arial, sans-serif;
  }
  .card {
    position: absolute;
    top: 242px;
    width: 520px;
    height: 300px;
    box-shadow: 0 6px 18px rgba(0,0,0,0.18);
    overflow: hidden;
  }
  /* Front side */
  .card-front {
    left: 50px;
    background: var(--navy);
    color: var(--white);
  }
  .front-title {
    position: absolute;
    left: 52px;
    top: 92px;
    margin: 0;
    font-size: 64px;
    font-weight: 700;
    letter-spacing: 2px;
    line-height: 1;
  }
  .front-rule {
    position: absolute;
    left: 52px;
    top: 164px;
    width: 410px;
    height: 1px;
    background: var(--white);
  }
  .front-text {
    position: absolute;
    left: 52px;
    top: 172px;
    width: 420px;
    margin: 0;
    font-size: 15px;
    line-height: 1.3;
  }
  .front-rule-end {
    position: absolute;
    left: 52px;
    top: 242px;
    width: 410px;
    height: 1px;
    background: var(--white);
  }
  /* Back side */
  .card-back {
    left: 630px;
    background: var(--white);
  }
  .back-band {
    position: absolute;
    left: 0; top: 0;
    width: 100%;
    height: 196px;
    background: var(--navy);
    color: var(--white);
  }
  .back-accent {
    position: absolute;
    left: 0;
    top: 201px;
    width: 100%;
    height: 3px;
    background: var(--navy);
  }
  .identity {
    position: absolute;
    left: 28px;
    top: 120px;
    margin: 0;
    display: flex;
    align-items: baseline;
    gap: 8px;
  }
  .identity-name {
    font-size: 21px;
    font-weight: 700;
  }
  .identity-divider {
    font-size: 22px;
  }
  .identity-role {
    font-size: 11px;
    letter-spacing: 0.8px;
  }
  .contacts {
    position: absolute;
    left: 28px;
    top: 154px;
    display: flex;
    gap: 26px;
    font-size: 13px;
  }
  .contact {
    display: flex;
    align-items: center;
    gap: 6px;
  }
  .contact svg { width: 13px; height: 13px; }
  .credentials {
    position: absolute;
    left: 28px;
    top: 218px;
    margin: 0;
    font-size: 13px;
    color: var(--ink);
  }
  .credentials strong { font-weight: 700; }
  .description {
    position: absolute;
    left: 28px;
    top: 240px;
    width: 470px;
    margin: 0;
    font-size: 12.5px;
    line-height: 1.45;
    color: var(--ink);
  }
</style>
</head>
<body>

<section class="card card-front" aria-label="Front of card">
  <h1 class="front-title">GOTTTD</h1>
  <div class="front-rule"></div>
  <p class="front-text">Diploma of Community Counselling And the following affiliation Guild of Talk Therapists of Tasvale and District Inc.</p>
  <div class="front-rule-end"></div>
</section>

<section class="card card-back" aria-label="Back of card">
  <div class="back-band">
    <p class="identity">
      <span class="identity-name">Dr Henry Walsh</span>
      <span class="identity-divider">|</span>
      <span class="identity-role">COUNSELLING SERVICES</span>
    </p>
    <div class="contacts">
      <span class="contact">
        <svg viewBox="0 0 16 16" aria-hidden="true"><path fill="#ffffff" d="M3.5 1.5l2.2 0 1 3.2-1.5 1.2c.8 1.8 2.1 3.1 3.9 3.9l1.2-1.5 3.2 1v2.2c0 .8-.7 1.5-1.5 1.5C6.6 13 3 9.4 2 3c0-.8.7-1.5 1.5-1.5z"/></svg>
        04.55.83.7190
      </span>
      <span class="contact">
        <svg viewBox="0 0 16 16" aria-hidden="true"><rect x="1" y="3" width="14" height="10" fill="#ffffff"/><path d="M1.5 3.5L8 9l6.5-5.5" fill="none" stroke="#0c2249" stroke-width="1.4"/></svg>
        Henry.Walsh937@mailbrook.example
      </span>
    </div>
  </div>
  <div class="back-accent"></div>
  <p class="credentials"><strong>BSc</strong> (Psychology) &bull; <strong>BA hons</strong> (Philosophy) &bull; <strong>PhD</strong> (Philosophy)</p>
  <p class="description">Counselling Services and the practice focuses on philosophical narrative and existential counselling for individuals, couples and families.</p>
</section>

</body>
</html>
```